Business Card for Financial Asset Management Company

Now we are launching a new company based in Tokyo.
The company information is below;

Company Name: Caldera Stewardship

Operations: Financial assets management, Proposing forming portfolio of assets, Consulting service, and advising to enhance your company's financial health

Corporate Colour: Japan Blue or Navy like below
http://pages.art.velmoreu.edu/tkovan/images/Indigo/Aqua-Indigo-104.jpg

It's dark and deep, and will get to fit to our clients as our relationships last longer and longer.

Our images for this colour are "Japanese style" and "pride in our craftmanship" , and also "gentle".

Corporate Key Image: an order taker who is sincere, polite, but courageous

We don't have our logo yet so please feel free to put any symbol on your design.

Please do not hesitate about asking any questions.
Thank you :-)

Reason: We are still discussin on final decision. Thank you for your understanding.

```html
<!DOCTYPE html>
<html lang="en">
<head>
<meta charset="utf-8">
<title>Caldera Stewardship — Business Card</title>
<link rel="stylesheet" href="https://fonts.googleapis.com/css2?family=Open+Sans:wght@400;600;700&display=swap">
<style>
  :root {
    --backdrop: #8a8a8c;
    --indigo-deep: #12132b;
    --indigo-mid: #1e1d47;
    --indigo-glow: #30297a;
    --brand-text: #2f2a72;
    --ink: #1f1f24;
    --muted: #7a7a80;
    --rule: #9a9aa0;
    --paper: #ffffff;
  }
  * { margin: 0; padding: 0; box-sizing: border-box; }
  html, body {
    width: 1200px; height: 1000px; overflow: hidden;
    background: var(--backdrop);
    font-family: "Open Sans", Arial, sans-serif;
  }
  .canvas { position: relative; width: 1200px; height: 1000px; }

  .card-back {
    position: absolute; left: 360px; top: 97px; width: 753px; height: 440px;
    background: linear-gradient(90deg, var(--indigo-deep) 0%, var(--indigo-mid) 30%, var(--indigo-glow) 52%, var(--indigo-mid) 75%, var(--indigo-deep) 100%);
  }
  .card-back .back-wordmark {
    position: absolute; left: 0; right: 0; top: 195px;
    text-align: center; color: var(--paper);
    font-size: 34px; font-weight: 600; letter-spacing: 0.2px;
  }

  .card-front {
    position: absolute; left: 56px; top: 432px; width: 753px; height: 443px;
    background: var(--paper); overflow: hidden;
  }
  .front-band { position: absolute; left: 0; bottom: 0; width: 753px; height: 100px; }

  .brand { position: absolute; left: 138px; top: 112px; display: flex; align-items: center; }
  .brand-mark { width: 44px; height: 44px; background: var(--brand-text); margin-right: 20px; }
  .brand-name { color: var(--brand-text); font-size: 31px; font-weight: 600; line-height: 1; }

  .person { position: absolute; left: 153px; top: 254px; }
  .person-name { color: var(--brand-text); font-size: 22px; font-weight: 700; line-height: 1.2; }
  .person-role { color: var(--muted); font-size: 18px; margin-top: 4px; }

  .divider { position: absolute; left: 333px; top: 216px; width: 1px; height: 150px; background: var(--rule); }

  .contact { position: absolute; left: 350px; top: 212px; color: var(--ink); font-size: 18px; }
  .address { line-height: 28px; }
  .contact-line { display: flex; align-items: center; height: 34px; }
  .contact-line svg { width: 18px; height: 16px; margin-right: 12px; fill: var(--brand-text); }
  .contact-line.phone { margin-top: 6px; }
</style>
</head>
<body>
<main class="canvas">
  <section class="card-back">
    <div class="back-wordmark">Caldera Stewardship</div>
  </section>

  <section class="card-front">
    <div class="brand">
      <span class="brand-mark"></span>
      <span class="brand-name">Caldera Stewardship</span>
    </div>

    <div class="person">
      <div class="person-name">Mayu Sorano</div>
      <div class="person-role">Financial Advisor</div>
    </div>

    <div class="divider"></div>

    <div class="contact">
      <div class="address">Kasumi Hill Building, 2-7-4<br>Hanazono Minato-ku, Tokyo</div>
      <div class="contact-line phone">
        <svg viewBox="0 0 18 16"><path d="M2 5c0-2 3-3 7-3s7 1 7 3v1.5h-4V5H6v1.5H2z"/><path d="M5 8h8l2 6H3z"/></svg>
        81-6-4870-2291
      </div>
      <div class="contact-line">
        <svg viewBox="0 0 18 16"><rect x="5" y="1" width="8" height="4"/><rect x="1" y="6" width="16" height="6" rx="1"/><rect x="5" y="11" width="8" height="4"/></svg>
        81-6-4870-22915
      </div>
      <div class="contact-line">
        <svg viewBox="0 0 18 16"><path d="M2 3h14v10H2z M3 4l6 5 6-5" fill="none" stroke="#2f2a72" stroke-width="1.3"/></svg>
        info@calderastewardship.jp
      </div>
    </div>

    <svg class="front-band" viewBox="0 0 753 100" preserveAspectRatio="none">
      <defs>
        <linearGradient id="band-fade" x1="0" x2="1" y1="0" y2="0">
          <stop offset="0" stop-color="#1a1b38"/>
          <stop offset="0.3" stop-color="#1f1d4a"/>
          <stop offset="0.5" stop-color="#30297a"/>
          <stop offset="0.72" stop-color="#1f1d4a"/>
          <stop offset="1" stop-color="#1a1b38"/>
        </linearGradient>
      </defs>
      <path d="M0 7 Q376 97 753 7 L753 100 L0 100 Z" fill="url(#band-fade)"/>
    </svg>
  </section>
</main>
</body>
</html>
```